Brine KLV - Website

Brine KLV is a online marketing solutions Agency, working with top partners within the industry to deliver online customers to Digital campaigns.

Our current site is www.brineklv.example (Apart from the logo, there is NOTHING we like about this site - please do not repeat anything from this site)

Specification of website:

- Modern, and light refreshing look. Corporate and neutral designs.

-Keep our logo - colour theme: Green/grey - hint of Orange/Blue

- The only text we would like on the Homepage is: Performance based online marketing specialists, driving incremental sales globally

and...

These are headings we would like people to do: Affiliate Marketing, Email marketing, Lead Generation, Social media marketing, Search Engine Marketing, Incentive Marketing (there is no need for the detailed text of these topics to be on front page, these can be linked into another page for those who seeks further info)

Images: Have images to show what we do.. keep it neat and professional/simple and stylish.

Please contact us if you have any questions at all.

Thank you for taking time our with our project!

Good luck all!

Regards

Brine KLV
Updates

Hello Designers,

Thank you to all who have taken time out working on our project. We have been very happy with the quality and level of prompt feedback.

Unfortunately we could only choose one, and MoonVex's designed is most suited for our company branding. So, Congratulations MoonVex.

Once again, thank you all.

Kindest regards,

Brine KLV

Target Market(s)

Clients: Fizzo, Torvik, Lunco, pelbet.example, Varnell Hotel...

Industry/Entity Type

Marketing

Requirements
Must have
• User friendly
Nice to have
• We operate Internationally, so a generic feel for EU/UK/US would be ideal...
Should not have
• Should not look like www.brineklv.example

```html
<!DOCTYPE html>
<html lang="en">
<head>
<meta charset="utf-8">
<title>Brine KLV – Performance based online marketing</title>
<link rel="stylesheet" href="https://fonts.googleapis.com/css2?family=Gelasio:wght@400;700&family=Arimo:wght@400;700&display=swap">
<style>
  :root {
    --green: #7cb82f;
    --green-light: #a8d65c;
    --green-dark: #4f8a15;
    --grey: #b9b9b9;
    --grey-dark: #8d8d8d;
    --text: #222;
    --hero-grey: #9a9a9a;
    --white: #fff;
  }
  * { box-sizing: border-box; margin: 0; padding: 0; }
  html, body { width: 1200px; height: 1122px; overflow: hidden; }
  body {
    position: relative;
    font-family: "Arimo", Arial, sans-serif;
    color: var(--text);
    background: linear-gradient(#fff 0, #fff 456px, #f6f6f6 470px, #ececec 1030px);
  }
  .header-grid {
    position: absolute; left: 0; top: 0; width: 1200px; height: 240px;
    background-image:
      linear-gradient(rgba(124,184,47,.12) 1px, transparent 1px),
      linear-gradient(90deg, rgba(124,184,47,.12) 1px, transparent 1px);
    background-size: 12px 12px;
    -webkit-mask-image: linear-gradient(#000, transparent);
    mask-image: linear-gradient(#000, transparent);
  }
  .brand {
    position: absolute; left: 94px; top: 38px;
    font-family: "Arimo", Arial, sans-serif; font-size: 40px; font-weight: 700;
    line-height: 48px; color: var(--green);
  }
  .quote-tab {
    position: absolute; left: 900px; top: 0; width: 184px; height: 40px;
    background: linear-gradient(#d4d4d4, #a9a9a9);
    border-radius: 0 0 6px 6px;
    display: flex; align-items: center; justify-content: center; gap: 10px;
    font-family: "Gelasio", Georgia, serif; font-size: 19px; font-weight: 700; color: var(--white);
  }
  .main-nav {
    position: absolute; left: 360px; top: 84px; width: 754px; height: 44px;
    background: linear-gradient(var(--green-light), var(--green) 55%, var(--green-dark));
    border-radius: 6px; display: flex; overflow: hidden;
    box-shadow: 0 3px 5px rgba(0,0,0,.15);
  }
  .main-nav a {
    font-family: "Gelasio", Georgia, serif; font-size: 18px; color: var(--white);
    text-decoration: none; display: flex; align-items: center; justify-content: center;
    height: 100%; padding: 0 22px;
  }
  .main-nav a.active { background: linear-gradient(#cfcfcf, #a3a3a3); width: 96px; padding: 0; }
  .hero {
    position: absolute; left: 80px; top: 140px; width: 1034px; height: 316px;
    background: var(--white); border-radius: 8px 8px 0 0;
    box-shadow: 0 0 8px rgba(0,0,0,.12);
  }
  .hero-arrow { position: absolute; top: 116px; }
  .hero-arrow.prev { left: 18px; }
  .hero-arrow.next { right: 20px; }
  .hero-title {
    position: absolute; left: 76px; top: 92px;
    font-family: "Gelasio", Georgia, serif; font-weight: 400; font-size: 34px; line-height: 44px;
    color: var(--green);
  }
  .hero-title .caps { color: var(--hero-grey); }
  .hero-visual {
    position: absolute; left: 700px; top: 30px; width: 220px; height: 250px;
    background: radial-gradient(circle at 45% 45%, #6fae2e, #bde29a 60%, transparent 72%);
  }
  .service { position: absolute; width: 252px; }
  .service-head {
    height: 50px; border-radius: 8px;
    background: linear-gradient(var(--green-light), var(--green) 55%, var(--green-dark));
    box-shadow: 0 3px 5px rgba(0,0,0,.2);
    display: flex; align-items: center; padding-left: 8px; gap: 12px;
  }
  .service-icon {
    width: 46px; height: 46px; border-radius: 8px; background: var(--white);
    display: flex; align-items: center; justify-content: center; flex: none;
  }
  .service-title {
    font-family: "Gelasio", Georgia, serif; font-size: 17px; line-height: 19px;
    color: var(--white); text-align: center; flex: 1; padding-right: 10px;
  }
  .service p {
    margin: 26px 0 0 18px; width: 212px; height: 112px;
    font-size: 12.5px; line-height: 16px; color: var(--text);
  }
  .more-info {
    display: inline-flex; align-items: center; gap: 6px; margin-left: 10px;
    padding: 3px 12px; border-radius: 12px;
    background: linear-gradient(#cfcfcf, #9c9c9c);
    color: var(--white); font-family: "Gelasio", Georgia, serif; font-size: 14px; text-decoration: none;
  }
  .site-footer {
    position: absolute; left: 0; top: 1030px; width: 1200px; height: 92px;
    background: #dcdcdc; text-align: center; font-size: 11px; color: #333;
  }
  .footer-nav { margin-top: 30px; display: flex; justify-content: center; gap: 28px; }
  .footer-nav a { color: #333; text-decoration: none; }
  .copyright { margin-top: 16px; }
</style>
</head>
<body>
  <div class="header-grid"></div>

  <div class="brand">Brine KLV</div>

  <a class="quote-tab">
    <svg width="18" height="22" viewBox="0 0 18 22"><path d="M4 1 L8 1 L9 6 L6 8 Q8 13 12 16 L14 13 L18 15 L17 20 Q9 22 3 12 Q0 5 4 1Z" fill="#fff"/></svg>
    Get a Quote !
  </a>

  <nav class="main-nav">
    <a class="active">home</a>
    <a>about us</a>
    <a>what we do</a>
    <a>our work</a>
    <a>work with us</a>
    <a>contact us</a>
  </nav>

  <section class="hero">
    <svg class="hero-arrow prev" width="24" height="50" viewBox="0 0 24 50"><path d="M20 3 L4 25 L20 47" stroke="#cfcfcf" stroke-width="4" fill="none"/></svg>
    <h1 class="hero-title">Performance based<br><span class="caps">ONLINE MARKETING</span> specialists,<br>driving incremental sales globally</h1>
    <div class="hero-visual" role="img" aria-label="Green dart hitting a bullseye target"></div>
    <svg class="hero-arrow next" width="24" height="50" viewBox="0 0 24 50"><path d="M4 3 L20 25 L4 47" stroke="#cfcfcf" stroke-width="4" fill="none"/></svg>
  </section>

  <article class="service" style="left:72px; top:516px;">
    <div class="service-head">
      <span class="service-icon"><svg width="30" height="22" viewBox="0 0 30 22"><rect x="1" y="1" width="28" height="20" rx="2" fill="#3c7fd1"/><path d="M1 2 L15 13 L29 2" stroke="#fff" stroke-width="2" fill="none"/></svg></span>
      <span class="service-title">Email<br>Marketing</span>
    </div>
    <p>People aged between 18 and 24 spend an average of 31 hours a month checking their inboxes. Study has shown that email marketing will remain an essential tool in marketing for a long time to come.</p>
    <a class="more-info">more info ▸</a>
  </article>

  <article class="service" style="left:342px; top:516px;">
    <div class="service-head">
      <span class="service-icon"><svg width="30" height="26" viewBox="0 0 30 26"><rect x="10" y="1" width="10" height="6" rx="2" stroke="#7a3f12" stroke-width="2" fill="none"/><rect x="1" y="6" width="28" height="19" rx="3" fill="#a4571b"/></svg></span>
      <span class="service-title">Lead<br>Generation</span>
    </div>
    <p>This channel remains one of the most powerful acquisition methods in marketing. At Brine KLV we understand that to harness the true power of lead gen you have to balance quantity with quality.</p>
    <a class="more-info">more info ▸</a>
  </article>

  <article class="service" style="left:610px; top:516px;">
    <div class="service-head">
      <span class="service-icon"><svg width="30" height="28" viewBox="0 0 30 28"><rect x="2" y="12" width="7" height="15" fill="#3c7fd1"/><rect x="11" y="4" width="7" height="23" fill="#7cb82f"/><rect x="20" y="9" width="7" height="18" fill="#f0b020"/></svg></span>
      <span class="service-title">Incentive<br>Marketing</span>
    </div>
    <p>It is a $46bn+ a year industry because it drives very high volumes of traffic at low costs and should never be ruled out without careful consideration.</p>
    <a class="more-info">more info ▸</a>
  </article>

  <article class="service" style="left:876px; top:516px;">
    <div class="service-head">
      <span class="service-icon"><svg width="30" height="26" viewBox="0 0 30 26"><path d="M3 2 H27 Q29 2 29 4 V16 Q29 18 27 18 H12 L6 24 V18 H3 Q1 18 1 16 V4 Q1 2 3 2Z" fill="#e8893a"/></svg></span>
      <span class="service-title">Social Media<br>Marketing</span>
    </div>
    <p>Brine KLV and its partners have consistently been at the forefront of this new media, helping to pioneer new monetisation methods and strategies.</p>
    <a class="more-info">more info ▸</a>
  </article>

  <article class="service" style="left:68px; top:770px;">
    <div class="service-head">
      <span class="service-icon"><svg width="30" height="30" viewBox="0 0 30 30"><circle cx="12" cy="12" r="9" stroke="#3c7fd1" stroke-width="3" fill="#cfe3f7"/><path d="M19 19 L28 28" stroke="#555" stroke-width="4"/></svg></span>
      <span class="service-title">Search Engine<br>Marketing</span>
    </div>
    <p>People aged between 18 and 24 spend an average of 31 hours a month checking their inboxes. Study has shown that email marketing will remain an essential tool in marketing for a long time to come.</p>
    <a class="more-info">more info ▸</a>
  </article>

  <article class="service" style="left:336px; top:770px;">
    <div class="service-head">
      <span class="service-icon"><svg width="30" height="30" viewBox="0 0 30 30"><circle cx="12" cy="12" r="9" stroke="#7cb82f" stroke-width="3" fill="none"/><path d="M12 7 V17 M7 12 H17" stroke="#7cb82f" stroke-width="3"/><path d="M19 19 L28 28" stroke="#555" stroke-width="4"/></svg></span>
      <span class="service-title">Search Engine<br>Optimization</span>
    </div>
    <p>This channel remains one of the most powerful acquisition methods in marketing. At Brine KLV we understand that to harness the true power of lead gen you have to balance quantity with quality.</p>
    <a class="more-info">more info ▸</a>
  </article>

  <article class="service" style="left:606px; top:770px;">
    <div class="service-head">
      <span class="service-icon"><svg width="30" height="30" viewBox="0 0 30 30"><path d="M6 28 L9 20 L24 3 L28 7 L13 24 Z" fill="#a35a3a"/><path d="M6 28 L9 20 L13 24 Z" fill="#333"/></svg></span>
      <span class="service-title">Custom<br>Web Design</span>
    </div>
    <p>It is a $46bn+ a year industry because it drives very high volumes of traffic at low costs and should never be ruled out without careful consideration.</p>
    <a class="more-info">more info ▸</a>
  </article>

  <article class="service" style="left:870px; top:770px;">
    <div class="service-head">
      <span class="service-icon"><svg width="30" height="30" viewBox="0 0 30 30"><rect x="4" y="2" width="22" height="26" rx="2" fill="#f3f3f3" stroke="#888" stroke-width="1.5"/><path d="M8 9 H22 M8 14 H22 M8 19 H18" stroke="#3c7fd1" stroke-width="2"/></svg></span>
      <span class="service-title">Account<br>Management</span>
    </div>
    <p>Brine KLV and its partners have consistently been at the forefront of this new media, helping to pioneer new monetisation methods and strategies.</p>
    <a class="more-info">more info ▸</a>
  </article>

  <footer class="site-footer">
    <nav class="footer-nav">
      <a>Home</a><span>|</span><a>About Us</a><span>|</span><a>What we Do</a><span>|</span><a>Our work</a><span>|</span><a>Work with us</a><span>|</span><a>Contact Us</a>
    </nav>
    <p class="copyright">Copyright © 2010 Brine KLV. All Rights Reserved.</p>
  </footer>
</body>
</html>
```